Comprehensive Branding Development for Brightvale Holdings Limited

We have our logo and are seeking a talented graphic designer to help us develop a cohesive branding guideline based on this logo provided by our client.
The goal is to create a comprehensive branding package for various office stationery items and promotional materials.

Deliverables:

The designer will be responsible for creating branding guidelines for the following items:

Letterhead
Envelope
Business card
Key holders
T-shirts
Face cap
Car branding
Pen
Dangler (Air Fresheners)
Lapel pin
PowerPoint template
ID card
Carrier bag
Notebook
Mug cup
Umbrella

Logo Text

Logo Provided by client and no needs for designing a new logo

```html
<!DOCTYPE html>
<html lang="en">
<head>
<meta charset="utf-8">
<title>Brightvale Holdings Limited – Stationery</title>
<link href="https://fonts.googleapis.com/css2?family=Montserrat:wght@400;600;700&family=Oswald:wght@500&family=Open+Sans:wght@400;600&display=swap" rel="stylesheet">
<style>
:root{
  --red:#e1262c;
  --red-dark:#c41a20;
  --grey:#6f6f6f;
  --ink:#2b2b2b;
  --card-dark:#2a2a2c;
  --white:#ffffff;
  --bg-cards:#d8d8d8;
  --bg-letter:#8fb3c6;
  --bg-pen:#22a7db;
  --bg-id:#a4c9f0;
  --bg-tag:#3d4145;
  --bg-envelope:#e6e4e0;
}
*{box-sizing:border-box;margin:0;padding:0}
html,body{width:1200px;height:4919px;overflow:hidden}
body{font-family:"Open Sans",sans-serif;color:var(--ink)}
.panel{position:relative;width:1200px;overflow:hidden}
.panel--cards{height:831px;background:var(--bg-cards)}
.panel--letter{height:831px;background:var(--bg-letter)}
.panel--pen{height:832px;background:var(--bg-pen)}
.panel--id{height:755px;background:var(--bg-id)}
.panel--tag{height:840px;background:var(--bg-tag)}
.panel--envelope{height:830px;background:var(--bg-envelope)}

/* brand name lockup */
.brand{display:flex;align-items:center;gap:10px;font-family:"Montserrat",sans-serif;font-weight:600;color:var(--red);text-transform:uppercase;line-height:1.05}
.brand__mark{width:26px;height:26px;background:var(--red);flex:none}
.brand--white{color:var(--white)}
.brand--white .brand__mark{background:var(--white)}

.contact{list-style:none;display:flex;flex-direction:column;gap:8px;font-size:14px}
.contact li{display:flex;align-items:center;gap:10px}
.icon{width:20px;height:20px;flex:none}

/* business cards */
.bcard{position:absolute;width:500px;height:290px;background:var(--card-dark);border-radius:4px;color:var(--white)}
.bcard--front{left:70px;top:270px;padding:40px}
.bcard--back{left:630px;top:270px;display:flex;align-items:center;justify-content:center}
.bcard .brand{font-size:24px}
.bcard__person{position:absolute;right:40px;top:40px;text-align:right}
.bcard__name{font-family:"Montserrat",sans-serif;font-weight:700;font-size:18px}
.bcard__role{font-size:14px;color:#cfcfcf}
.bcard .contact{position:absolute;left:40px;bottom:36px;color:#e8e8e8;font-size:13px}

/* letterhead */
.letter{position:absolute;left:340px;top:40px;width:520px;height:750px;background:var(--white);padding:40px 44px;box-shadow:0 6px 20px rgba(0,0,0,.15)}
.letter .brand{font-size:22px}
.letter__rule{display:flex;align-items:flex-end;gap:14px;margin-top:20px}
.letter__rule span{flex:1;height:2px;background:var(--red)}
.letter__company{font-family:"Oswald",sans-serif;font-weight:500;font-size:15px;color:var(--ink)}
.letter__greeting{font-family:"Montserrat",sans-serif;font-weight:700;font-size:20px;margin:34px 0 16px}
.letter__body p{font-size:10.5px;line-height:1.7;color:#555;margin-bottom:12px}
.letter__sign{margin-top:26px;width:120px;border-bottom:1px solid #999;height:26px}
.letter__signer{font-size:10px;color:#777;margin-top:6px}
.letter .contact{position:absolute;left:44px;bottom:80px;font-size:12px}
.pattern-band{position:absolute;left:0;right:0;height:28px;background:repeating-linear-gradient(90deg,var(--red) 0 18px,#f3c9ca 18px 24px)}
.letter .pattern-band{bottom:20px}

/* pen */
.pen{position:absolute;left:70px;top:330px}

/* ID card */
.lanyard{position:absolute;left:590px;top:0;width:70px;height:140px;background:var(--white);border-left:6px solid var(--red);border-right:6px solid var(--red)}
.clip{position:absolute;left:605px;top:140px;width:40px;height:60px;border:6px solid #b8bcc2;border-radius:14px}
.idcard{position:absolute;left:425px;top:190px;width:400px;height:520px;border-radius:18px;overflow:hidden;background:var(--white);box-shadow:0 8px 24px rgba(0,0,0,.15)}
.idcard__slot{position:absolute;left:170px;top:18px;width:60px;height:12px;border-radius:6px;background:var(--bg-id)}
.idcard__head{height:170px;display:flex;align-items:center;justify-content:center}
.idcard .brand{font-size:26px}
.idcard__body{position:absolute;top:170px;left:0;right:0;bottom:0;background:var(--red);text-align:center;color:var(--white)}
.idcard__photo{width:160px;height:160px;border-radius:50%;border:6px solid var(--white);margin:-40px auto 0;background:radial-gradient(circle at 50% 40%,#c9c2bc,#6d6a68)}
.idcard__name{font-family:"Montserrat",sans-serif;font-weight:700;font-size:30px;margin-top:24px;letter-spacing:.5px}
.idcard__role{font-family:"Montserrat",sans-serif;font-weight:600;font-size:15px;margin-top:4px}
.idcard__mail{display:flex;align-items:center;justify-content:center;gap:8px;font-size:15px;margin-top:38px}

/* hanging tag */
.string{position:absolute;left:599px;top:0;width:2px;height:170px;background:#c79a5b}
.tag{position:absolute;left:510px;top:170px;width:180px;height:300px;background:var(--white);padding:30px 16px 0}
.tag .brand{font-size:15px;gap:6px}
.tag .brand__mark{width:16px;height:16px}
.tag .contact{margin-top:46px;font-size:10px;gap:8px}
.tag .icon{width:14px;height:14px}
.tag .pattern-band{bottom:20px;height:18px}

/* envelope */
.envelope{position:absolute;left:250px;top:250px;width:700px;height:330px;background:var(--white);box-shadow:0 6px 18px rgba(0,0,0,.12)}
.envelope__flap{height:120px;background:var(--red);display:flex;align-items:center;justify-content:center}
.envelope .brand{font-size:28px}
.envelope .contact{flex-direction:row;justify-content:space-around;margin-top:120px;font-size:14px}
</style>
</head>
<body>

<svg width="0" height="0" style="position:absolute">
  <defs>
    <symbol id="i-phone" viewBox="0 0 24 24"><circle cx="12" cy="12" r="11" fill="none" stroke="currentColor" stroke-width="2"/><path d="M8 7l2-1 1.5 3-1.3 1a6 6 0 0 0 3 3l1-1.3 3 1.5-1 2c-4 0-8.2-4.2-8.2-8.2z" fill="currentColor"/></symbol>
    <symbol id="i-mail" viewBox="0 0 24 24"><circle cx="12" cy="12" r="11" fill="none" stroke="currentColor" stroke-width="2"/><rect x="6.5" y="8" width="11" height="8" fill="none" stroke="currentColor" stroke-width="1.6"/><path d="M6.5 8l5.5 4.5L17.5 8" fill="none" stroke="currentColor" stroke-width="1.6"/></symbol>
    <symbol id="i-web" viewBox="0 0 24 24"><circle cx="12" cy="12" r="11" fill="none" stroke="currentColor" stroke-width="2"/><circle cx="12" cy="12" r="5.5" fill="none" stroke="currentColor" stroke-width="1.5"/><path d="M6.5 12h11M12 6.5v11" stroke="currentColor" stroke-width="1.2"/></symbol>
  </defs>
</svg>

<!-- Business cards -->
<section class="panel panel--cards">
  <article class="bcard bcard--front">
    <div class="brand"><span class="brand__mark"></span>Brightvale<br>Holdings Limited</div>
    <div class="bcard__person"><div class="bcard__name">Name</div><div class="bcard__role">Occupation</div></div>
    <ul class="contact">
      <li><svg class="icon" style="color:var(--white)"><use href="#i-phone"/></svg>(555) 010-2468</li>
      <li><svg class="icon" style="color:var(--white)"><use href="#i-mail"/></svg>info@brightvale.finance</li>
      <li><svg class="icon" style="color:var(--white)"><use href="#i-web"/></svg>brightvale.finance</li>
    </ul>
  </article>
  <article class="bcard bcard--back">
    <div class="brand" style="font-size:30px"><span class="brand__mark"></span>Brightvale<br>Holdings Limited</div>
  </article>
</section>

<!-- Letterhead -->
<section class="panel panel--letter">
  <article class="letter">
    <div class="brand"><span class="brand__mark"></span>Brightvale<br>Holdings Limited</div>
    <div class="letter__rule"><span></span><div class="letter__company">Brightvale Holdings Limited</div></div>
    <h2 class="letter__greeting">Hello, world!</h2>
    <div class="letter__body">
      <p>Thank you for your continued trust in our team. This letter confirms the details of our recent meeting and outlines the next steps we agreed to take together.</p>
      <p>Our advisors will review your portfolio goals and prepare a clear plan for the coming quarter. You will receive a summary before our next call.</p>
      <p>Please reach out at any time with questions. We look forward to working with you.</p>
    </div>
    <div class="letter__sign"></div>
    <div class="letter__signer">Owen Hale, co-founder</div>
    <ul class="contact">
      <li><svg class="icon" style="color:var(--red)"><use href="#i-phone"/></svg>(555) 010-2468</li>
      <li><svg class="icon" style="color:var(--red)"><use href="#i-mail"/></svg>info@brightvale.finance</li>
      <li><svg class="icon" style="color:var(--red)"><use href="#i-web"/></svg>brightvale.finance</li>
    </ul>
    <div class="pattern-band" role="img" aria-label="Red decorative brand pattern band"></div>
  </article>
</section>

<!-- Pen -->
<section class="panel panel--pen">
  <svg class="pen" width="1060" height="170" viewBox="0 0 1060 170">
    <path d="M0 85 L60 70 L60 100 Z" fill="#555"/>
    <path d="M60 62 L200 50 L200 120 L60 108 Z" fill="var(--red)"/>
    <rect x="200" y="46" width="760" height="78" rx="30" fill="var(--white)"/>
    <rect x="430" y="44" width="26" height="82" fill="var(--red)"/>
    <rect x="474" y="44" width="26" height="82" fill="var(--red)"/>
    <path d="M940 46 h60 a39 39 0 0 1 0 78 h-60 z" fill="var(--red)"/>
    <rect x="560" y="26" width="400" height="16" rx="8" fill="#c9ccd0"/>
    <rect x="260" y="72" width="26" height="26" fill="var(--red)"/>
    <text font-family="Montserrat, sans-serif" font-weight="600" font-size="22" fill="var(--red)">
      <tspan x="640" y="80">BRIGHTVALE</tspan>
      <tspan x="640" y="106">HOLDINGS LIMITED</tspan>
    </text>
  </svg>
</section>

<!-- ID card -->
<section class="panel panel--id">
  <div class="lanyard"></div>
  <div class="clip"></div>
  <article class="idcard">
    <div class="idcard__slot"></div>
    <div class="idcard__head"><div class="brand"><span class="brand__mark"></span>Brightvale<br>Holdings Limited</div></div>
    <div class="idcard__body">
      <div class="idcard__photo" role="img" aria-label="Staff portrait photo"></div>
      <div class="idcard__name">DANA MERCER</div>
      <div class="idcard__role">MARKETING DIRECTOR</div>
      <div class="idcard__mail"><svg class="icon" style="color:var(--white)"><use href="#i-mail"/></svg>info@brightvale.finance</div>
    </div>
  </article>
</section>

<!-- Hanging tag -->
<section class="panel panel--tag">
  <div class="string"></div>
  <article class="tag">
    <div class="brand"><span class="brand__mark"></span>Brightvale<br>Holdings Limited</div>
    <ul class="contact">
      <li><svg class="icon" style="color:var(--red)"><use href="#i-phone"/></svg>(555) 010-2468</li>
      <li><svg class="icon" style="color:var(--red)"><use href="#i-mail"/></svg>info@brightvale.finance</li>
      <li><svg class="icon" style="color:var(--red)"><use href="#i-web"/></svg>brightvale.finance</li>
    </ul>
    <div class="pattern-band" role="img" aria-label="Red decorative brand pattern band"></div>
  </article>
</section>

<!-- Envelope -->
<section class="panel panel--envelope">
  <article class="envelope">
    <div class="envelope__flap"><div class="brand brand--white"><span class="brand__mark"></span>Brightvale<br>Holdings Limited</div></div>
    <ul class="contact">
      <li><svg class="icon" style="color:var(--red)"><use href="#i-phone"/></svg>(555) 010-2468</li>
      <li><svg class="icon" style="color:var(--red)"><use href="#i-mail"/></svg>info@brightvale.finance</li>
      <li><svg class="icon" style="color:var(--red)"><use href="#i-web"/></svg>brightvale.finance</li>
    </ul>
  </article>
</section>

</body>
</html>
```